Premium CBD/Hemp company needs packaging and label design

Verdant Halcyon Labs, a premium CBD/Hemp company based in Scottsdale, Arizona is in need of a packaging and label design. We are launching with our flagship product which will be a 30 count capsule and will come in three functions: Pain Relief, Anxiety Support, and Sleep Support. For the purpose of this contest, please design packaging and label for our Anxiety Support product. Our products are physician formulated and all natural. Our main ingredient is CBD/Hemp and is complemented by specific herbs that synergistically work together to give the customer the most effective and desired result. We would like our branding to have a pharmaceutical look and feel with a focus on trust and transparency. We have uploaded our company logo that is to be used on both the packaging and label. We have also uploaded an executed branding questionnaire that will guide you to exactly what we are seeking to achieve as to the look and feel of our brand. Please feel free to contact us with any questions that you may have. The winner of this contest will have the opportunity to work with us on future projects as we will need packaging and label design for our entire Verdant Halcyon Labs product line.

Target Market(s)

See attached branding questionnaire

Industry/Entity Type

Health And Wellness

Font styles to use
Sans Serif

Colors

Designer to choose colors to be used in the design.

Requirements
Must have
• See attached branding questionnaire; Please superimpose labels onto a cobalt blue capsule bottle (see attached)
• >>UPON REVIEW of the FIRST 8 designs, we really like the silver, mildly metallic label background in DESIGN # 21300528, we do not want metalic lettering as that would not look very "Pharmaceutical"
• >>We are in search of a look that is a bit more "Pharmaceutical" than a look that would be more commonly found in a Supplement Store
Nice to have
• "See attached branding questionnaire
Should not have
• See attached branding questionnaire; NO marijuana or cannabis plant on the packaging or label

```html
<!DOCTYPE html>
<html lang="en">
<head>
<meta charset="utf-8">
<title>Verdant Halcyon Labs – Broad Spectrum CBD Packaging</title>
<link rel="stylesheet" href="https://fonts.googleapis.com/css2?family=Marcellus&family=Montserrat:wght@400;600&family=Oswald:wght@300;400&display=swap">
<style>
  :root{
    --cobalt:#2b40c8;
    --cobalt-deep:#1a2896;
    --silver-light:#ffffff;
    --silver-mid:#eef0f3;
    --silver-dark:#cfd4db;
    --ink:#1e1e1e;
    --green:#1f8a3a;
    --backdrop:#e9ebed;
  }
  *{margin:0;padding:0;box-sizing:border-box}
  html,body{width:1200px;height:1200px;overflow:hidden;background:var(--backdrop)}
  .canvas{position:relative;width:1200px;height:1200px;background:radial-gradient(circle at 50% 40%,#f7f8f9,var(--backdrop))}

  .display{font-family:"Marcellus",serif;color:var(--ink);text-align:center;line-height:.95}
  .brand{font-family:"Montserrat",sans-serif;font-weight:600;letter-spacing:.04em;display:flex;align-items:center;justify-content:center;gap:10px;white-space:nowrap}
  .brand-dot{width:22px;height:22px;border-radius:50%;border:2px solid currentColor;flex:none}
  .leaf-art{margin:0 auto;border-radius:40px;background:radial-gradient(ellipse at center,#b8bec6 0%,#dfe2e6 55%,rgba(255,255,255,0) 75%)}
  .molecule-mesh{position:absolute;background:radial-gradient(ellipse at center,rgba(120,145,205,.55),rgba(160,180,220,.2) 55%,rgba(255,255,255,0) 75%)}
  .badge{position:absolute}
  .strength{display:inline-block;background:linear-gradient(180deg,#fdfdfe,#d4d8de);border-radius:8px;padding:4px 14px 2px;text-align:center;box-shadow:0 1px 3px rgba(0,0,0,.2)}
  .strength-mg{font-family:"Montserrat",sans-serif;color:var(--ink);font-size:22px;line-height:1}
  .strength-mg small{font-size:12px}
  .strength-cbd{font-family:"Montserrat",sans-serif;font-weight:600;color:var(--cobalt);font-size:34px;line-height:1}
  .count{display:flex;align-items:center;gap:8px;font-family:"Oswald",sans-serif;font-weight:300;white-space:nowrap}

  /* ---------- carton ---------- */
  .carton-side,.carton-front{position:absolute;top:50px;height:580px;background:linear-gradient(160deg,var(--silver-light),var(--silver-mid) 60%,var(--silver-dark));overflow:hidden;box-shadow:0 8px 24px rgba(0,0,0,.12)}
  .carton-side{left:240px;width:300px}
  .carton-front{left:540px;width:420px}
  .band{position:absolute;left:0;width:100%}
  .carton-front .band-top{top:0;height:140px}
  .carton-front .band-bottom{bottom:0;height:100px}
  .carton-front .brand{position:absolute;top:42px;width:100%;color:#fff;font-size:21px}
  .carton-front .leaf-art{position:absolute;top:136px;left:140px;width:140px;height:40px}
  .carton-front .title{position:absolute;top:180px;width:100%}
  .carton-front .title-broad{font-size:48px}
  .carton-front .title-spectrum{font-size:36px;margin-top:4px}
  .carton-front .title-cbd{font-size:80px;margin-top:2px}
  .carton-front .rule{width:170px;height:2px;background:#8a9099;margin:4px auto 8px}
  .carton-front .subtitle{font-family:"Oswald",sans-serif;font-weight:300;font-size:16px;line-height:1.25;color:var(--ink);letter-spacing:.02em}
  .carton-front .strength{position:absolute;top:404px;left:160px;z-index:2}
  .carton-front .molecule-mesh{top:390px;width:100%;height:90px;left:0}
  .carton-front .badge-calm{left:30px;bottom:12px;width:74px;height:74px}
  .carton-front .badge-md{left:150px;bottom:6px;width:84px;height:84px}
  .carton-front .count{position:absolute;right:22px;bottom:22px;color:#fff;font-size:20px;flex-direction:column;gap:2px}

  .carton-side .band-top{top:0;height:50px}
  .carton-side .band-bottom{bottom:0;height:120px}
  .carton-side .spine{position:absolute;top:56px;left:34px;height:280px;writing-mode:vertical-rl;transform:rotate(180deg);display:flex;gap:6px;white-space:nowrap}
  .carton-side .spine-title{font-family:"Marcellus",serif;font-size:21px;color:var(--ink);letter-spacing:.02em}
  .carton-side .spine-sub{font-family:"Montserrat",sans-serif;font-size:8px;color:var(--ink);letter-spacing:.04em}
  .carton-side .copy{position:absolute;top:350px;left:34px;right:26px;font-family:"Oswald",sans-serif;font-weight:300;font-size:13px;line-height:1.75;color:#333;text-align:justify}
  .carton-side .molecule-mesh{top:430px;left:0;width:100%;height:70px}
  .carton-side .brand{position:absolute;bottom:36px;left:0;width:100%;color:#fff;font-size:15px}
  .carton-side .brand-dot{width:16px;height:16px}

  /* ---------- bottle label ---------- */
  .label{position:absolute;left:60px;top:690px;width:1080px;height:450px;box-shadow:0 8px 24px rgba(0,0,0,.12)}
  .label-ground{position:absolute;inset:0}
  .label-panel{position:absolute;left:240px;width:600px;top:0;height:100%}
  .label .brand{position:absolute;top:24px;width:100%;color:var(--cobalt);font-size:24px}
  .label .leaf-art{position:absolute;top:66px;left:220px;width:160px;height:46px}
  .label .title{position:absolute;top:116px;width:100%}
  .label .title-broad{font-size:56px}
  .label .title-spectrum{font-size:40px;margin-top:2px}
  .label .title-cbd{font-size:90px;margin-top:2px}
  .label .subtitle{font-family:"Montserrat",sans-serif;font-size:14px;letter-spacing:.04em;line-height:1.3;color:var(--ink);margin-top:6px}
  .label .bottom-row{position:absolute;top:352px;width:100%;display:flex;justify-content:center;align-items:center;gap:34px}
  .label .count{color:var(--ink);font-size:22px;font-weight:400}
  .label .mesh-left{left:0;bottom:0;width:180px;height:150px}
  .label .mesh-right{right:0;top:0;width:170px;height:170px}
  .label .badge-md{left:770px;top:70px;width:110px;height:110px}
  .label .badge-calm{left:222px;top:300px;width:96px;height:96px}
</style>
</head>
<body>
<main class="canvas">

  <section class="carton-side" aria-label="Carton side panel">
    <svg class="band band-top" viewBox="0 0 300 50" preserveAspectRatio="none"><path d="M0 0H300V22Q150 48 0 30Z" fill="var(--cobalt)"/><path d="M0 30Q150 48 300 22" stroke="#b9bec6" stroke-width="3" fill="none"/></svg>
    <div class="spine">
      <span class="spine-title">BROAD SPECTRUM CBD</span>
      <span class="spine-sub">CBD INFUSED PLANT BASED SUPPLEMENTS</span>
    </div>
    <p class="copy">Lorem ipsum dolor sit amet, consectetur adipiscing elit. Vestibulum quis mi vel eros rutrum et in lacus. Aliquam ipsum vitae suscipit. Pellentesque faucibus risus efficitur sodales, vel sodales nunc.</p>
    <div class="molecule-mesh" role="img" aria-label="Blue molecular mesh decoration"></div>
    <svg class="band band-bottom" viewBox="0 0 300 120" preserveAspectRatio="none"><path d="M0 30Q150 0 300 20V120H0Z" fill="var(--cobalt)"/><path d="M0 30Q150 0 300 20" stroke="#b9bec6" stroke-width="3" fill="none"/></svg>
    <div class="brand"><span class="brand-dot"></span>VERDANT HALCYON LABS</div>
  </section>

  <section class="carton-front" aria-label="Carton front panel">
    <svg class="band band-top" viewBox="0 0 420 140" preserveAspectRatio="none"><path d="M0 0H420V100Q210 170 0 100Z" fill="var(--cobalt)"/><path d="M0 100Q210 170 420 100" stroke="#b9bec6" stroke-width="4" fill="none"/></svg>
    <div class="brand"><span class="brand-dot"></span>VERDANT HALCYON LABS</div>
    <div class="leaf-art" role="img" aria-label="Silver leaves illustration"></div>
    <div class="title display">
      <div class="title-broad">BROAD</div>
      <div class="title-spectrum">SPECTRUM</div>
      <div class="title-cbd">CBD</div>
      <div class="rule"></div>
      <div class="subtitle">CBD INFUSED PLANT<br>BASED SUPPLEMENTS</div>
    </div>
    <div class="molecule-mesh" role="img" aria-label="Blue molecular mesh decoration"></div>
    <div class="strength"><div class="strength-mg">3000<small>MG</small></div><div class="strength-cbd">CBD</div></div>
    <svg class="band band-bottom" viewBox="0 0 420 130" preserveAspectRatio="none"><path d="M0 40Q210 -10 420 40V130H0Z" fill="var(--cobalt)"/><path d="M0 40Q210 -10 420 40" stroke="#b9bec6" stroke-width="4" fill="none"/></svg>
    <svg class="badge badge-calm" viewBox="0 0 100 100" aria-label="Anxiety support badge">
      <defs><path id="calmRingA" d="M50,50 m-37,0 a37,37 0 1,1 74,0 a37,37 0 1,1 -74,0"/></defs>
      <circle cx="50" cy="50" r="48" fill="#fff" stroke="#c3c8cf" stroke-width="3"/>
      <text font-family="Montserrat,sans-serif" font-size="9" fill="var(--cobalt)" letter-spacing="1"><textPath href="#calmRingA">ANXIETY SUPPORT • ANXIETY SUPPORT •</textPath></text>
      <circle cx="50" cy="50" r="26" fill="var(--cobalt)"/>
      <text x="50" y="55" text-anchor="middle" font-family="Montserrat,sans-serif" font-size="13" fill="#fff">CALM</text>
    </svg>
    <svg class="badge badge-md" viewBox="0 0 100 100" aria-label="Physician formulated badge">
      <defs><path id="mdRingA" d="M50,50 m-37,0 a37,37 0 1,1 74,0 a37,37 0 1,1 -74,0"/></defs>
      <circle cx="50" cy="50" r="48" fill="var(--cobalt-deep)" stroke="#c3c8cf" stroke-width="3"/>
      <text font-family="Montserrat,sans-serif" font-weight="600" font-size="10" fill="#fff" letter-spacing="1"><textPath href="#mdRingA">PHYSICIAN FORMULATED</textPath></text>
      <circle cx="50" cy="50" r="25" fill="var(--green)" stroke="#fff" stroke-width="2"/>
      <polygon points="50,36 62,43 62,57 50,64 38,57 38,43" fill="none" stroke="#fff" stroke-width="2"/>
    </svg>
    <div class="count">
      <svg width="30" height="22" viewBox="0 0 30 22"><rect x="3" y="2" width="9" height="18" rx="4.5" fill="none" stroke="#fff" stroke-width="2" transform="rotate(15 7 11)"/><rect x="17" y="2" width="9" height="18" rx="4.5" fill="#fff" transform="rotate(15 21 11)"/></svg>
      <span>30 CAPSULES</span>
    </div>
  </section>

  <section class="label" aria-label="Bottle label">
    <svg class="label-ground" viewBox="0 0 1080 450" preserveAspectRatio="none">
      <defs>
        <linearGradient id="silverFace" x1="0" y1="0" x2="1" y2="1">
          <stop offset="0" stop-color="#ffffff"/><stop offset=".6" stop-color="#eef0f3"/><stop offset="1" stop-color="#cfd4db"/>
        </linearGradient>
      </defs>
      <rect width="1080" height="450" fill="var(--cobalt)"/>
      <path d="M240 0H840Q785 225 840 450H240Q295 225 240 0Z" fill="url(#silverFace)" stroke="#c6cbd2" stroke-width="6"/>
    </svg>
    <div class="label-panel">
      <div class="molecule-mesh mesh-left" role="img" aria-label="Blue molecular mesh decoration"></div>
      <div class="molecule-mesh mesh-right" role="img" aria-label="Blue molecular mesh decoration"></div>
      <div class="brand"><span class="brand-dot"></span>VERDANT HALCYON LABS</div>
      <div class="leaf-art" role="img" aria-label="Silver leaves illustration"></div>
      <div class="title display">
        <div class="title-broad">BROAD</div>
        <div class="title-spectrum">SPECTRUM</div>
        <div class="title-cbd">CBD</div>
        <div class="subtitle">CBD INFUSED PLANT<br>BASED SUPPLEMENTS</div>
      </div>
      <div class="bottom-row">
        <div class="strength"><div class="strength-mg">3000<small>MG</small></div><div class="strength-cbd">CBD</div></div>
        <div class="count">
          <svg width="30" height="22" viewBox="0 0 30 22"><rect x="3" y="2" width="9" height="18" rx="4.5" fill="none" stroke="var(--cobalt)" stroke-width="2" transform="rotate(15 7 11)"/><rect x="17" y="2" width="9" height="18" rx="4.5" fill="var(--cobalt)" transform="rotate(15 21 11)"/></svg>
          <span>30 CAPSULES</span>
        </div>
      </div>
    </div>
    <svg class="badge badge-md" viewBox="0 0 100 100" aria-label="Physician formulated badge">
      <defs><path id="mdRingB" d="M50,50 m-37,0 a37,37 0 1,1 74,0 a37,37 0 1,1 -74,0"/></defs>
      <circle cx="50" cy="50" r="48" fill="var(--cobalt-deep)" stroke="#c3c8cf" stroke-width="3"/>
      <text font-family="Montserrat,sans-serif" font-weight="600" font-size="10" fill="#fff" letter-spacing="1"><textPath href="#mdRingB">PHYSICIAN FORMULATED</textPath></text>
      <circle cx="50" cy="50" r="25" fill="var(--green)" stroke="#fff" stroke-width="2"/>
      <polygon points="50,36 62,43 62,57 50,64 38,57 38,43" fill="none" stroke="#fff" stroke-width="2"/>
    </svg>
    <svg class="badge badge-calm" viewBox="0 0 100 100" aria-label="Anxiety support badge">
      <defs><path id="calmRingB" d="M50,50 m-37,0 a37,37 0 1,1 74,0 a37,37 0 1,1 -74,0"/></defs>
      <circle cx="50" cy="50" r="48" fill="#fff" stroke="var(--cobalt)" stroke-width="3"/>
      <text font-family="Montserrat,sans-serif" font-size="9" fill="var(--cobalt)" letter-spacing="1"><textPath href="#calmRingB">ANXIETY SUPPORT • ANXIETY SUPPORT •</textPath></text>
      <circle cx="50" cy="50" r="26" fill="var(--cobalt)"/>
      <text x="50" y="55" text-anchor="middle" font-family="Montserrat,sans-serif" font-size="13" fill="#fff">CALM</text>
    </svg>
  </section>

</main>
</body>
</html>
```